Flyer-Design für tamilisches Restaurant
Zielgruppe
Tamilisches Essen (kottu Rotti)
Aufgabenstellung
brauche eine zwei seitige A5 Flyer hoch oder quer spielt keine rolle das Hintergrund sollte Schwarz sein und paar Details in Gold wie unser Logo, das ist unsere Gedanke an design.
Auf der Vorderseite sollte, Neueröffnung am 01. März 2019 unser Hauptlogo, Facebook/ Instagram Logo in Gold mit unserer Seite (Selvo_Restaurant) und unser Motto #allaboutthebowl sein.
Auf der Rückseite, ein Bild mit kurzem Beschrieb ( Kottu Rotti das populärstes Gericht aus SriLanka)
Alle Gerichte zum mitnehmen und ab 8. März 2019 mit Lieferung.
unsere Öffnungszeiten
Montag bis Donnerstag 17.00 – 23.00 Uhr
Freitag 17.00 – 02.00 Uhr
Samstag 17.00 – 02.00 Uhr
Sonntag 17.00 – 23.00 Uhr
das Team von der Selvo freut such auf Ihren Besuch
Reservierungen unter 031 574 19 86
und noch unser Logo in klein Format

```html
<!DOCTYPE html>
<html lang="de">
<head>
<meta charset="utf-8">
<title>Selvo – Flyer Rückseite</title>
<link rel="stylesheet" href="https://fonts.googleapis.com/css2?family=Montserrat:wght@300;400;600&family=Nothing+You+Could+Do&display=swap">
<style>
  :root {
    --ink: #000000;
    --paper: #ffffff;
    --gold: #c9a94a;
    --caption: #1a1a1a;
    --photo-dark: #2a1a10;
    --photo-mid: #8a5a3a;
    --plate: #f2f1ef;
  }
  * { margin: 0; padding: 0; box-sizing: border-box; }
  html, body { width: 847px; height: 1200px; overflow: hidden; background: var(--ink); }
  .flyer {
    position: relative;
    width: 847px;
    height: 1200px;
    background: var(--ink);
    color: var(--paper);
    font-family: "Montserrat", sans-serif;
    overflow: hidden;
  }
  .announcement {
    position: absolute;
    left: 52px;
    top: 78px;
    width: 420px;
    text-align: center;
    text-transform: uppercase;
    font-weight: 400;
    font-size: 32px;
    line-height: 40px;
    letter-spacing: 1px;
    transform: rotate(-8deg);
    transform-origin: center;
  }
  .hours {
    position: absolute;
    left: 58px;
    top: 332px;
  }
  .hours__title {
    font-weight: 400;
    font-size: 31px;
    line-height: 40px;
    margin-bottom: 4px;
  }
  .hours__line {
    font-weight: 300;
    font-size: 25px;
    line-height: 40px;
  }
  .hours__reservation {
    font-weight: 300;
    font-size: 19px;
    line-height: 34px;
    letter-spacing: 0.5px;
  }
  .greeting {
    position: absolute;
    left: 80px;
    top: 632px;
    font-family: "Nothing You Could Do", cursive;
    color: var(--gold);
    font-size: 28px;
    transform: rotate(-3deg);
    transform-origin: left center;
    white-space: nowrap;
  }
  .dish-photo {
    position: absolute;
    left: 0;
    top: 690px;
    width: 847px;
    height: 510px;
    background: linear-gradient(to bottom, var(--ink) 0%, var(--photo-dark) 25%, var(--photo-mid) 50%, var(--plate) 85%, var(--plate) 100%);
  }
  .brand-mark {
    position: absolute;
    left: 700px;
    top: 1050px;
    display: flex;
    align-items: center;
    gap: 10px;
    font-family: "Montserrat", sans-serif;
    font-weight: 400;
    font-size: 38px;
    color: var(--gold);
  }
  .brand-mark__dot {
    width: 14px;
    height: 14px;
    border-radius: 50%;
    background: var(--gold);
  }
  .dish-caption {
    position: absolute;
    left: 55px;
    top: 1106px;
    color: var(--caption);
  }
  .dish-caption__name {
    font-weight: 600;
    font-size: 24px;
    line-height: 31px;
  }
  .dish-caption__text {
    font-weight: 400;
    font-size: 25px;
    line-height: 31px;
  }
</style>
</head>
<body>
  <main class="flyer">
    <h1 class="announcement">Alle Gerichte zum<br>Mitnehmen und<br>ab 8. März 2019<br>mit Lieferung</h1>

    <section class="hours">
      <h2 class="hours__title">Unsere Öffnungszeiten</h2>
      <p class="hours__line">Montag bis Donnerstag 17.00 – 23.00 Uhr</p>
      <p class="hours__line">Freitag 17.00 – 02.00 Uhr</p>
      <p class="hours__line">Samstag 17.00 – 02.00 Uhr</p>
      <p class="hours__line">Sonntag 17.00 – 23.00 Uhr</p>
      <p class="hours__reservation">Reservierungen unter 031 574 19 86</p>
    </section>

    <p class="greeting">Das Team von Selvo freut sich auf Ihren Besuch!</p>

    <div class="dish-photo" role="img" aria-label="Foto: Kottu Rotti auf einem weißen Teller mit Zitronenscheibe, Petersilie und roten Zwiebelringen"></div>

    <div class="brand-mark"><span class="brand-mark__dot"></span>Selvo</div>

    <div class="dish-caption">
      <p class="dish-caption__name">Kottu Rotti</p>
      <p class="dish-caption__text">das populärstes Gericht aus SriLanka</p>
    </div>
  </main>
</body>
</html>
```